Recreate circuit style graphics for a carnival ride

- Design circuit style graphics for front panel 70” W x 51” H
- Create side panel graphics with WhirlCove font and Revel IN Bloom Logo 34" H x 42 3/4" W
- Include 1” bleed for printing

Recreate Whirl Cove Trailer - Graphic
1 - 6"H x 120" W
1 - 6"H x 171.5" W

Delivery in .Illustrator (.AI)
Print-ready PDF (PDF/X-4)

Amusement/ carnival

• Matching design

```html
<!DOCTYPE html>
<html lang="en">
<head>
<meta charset="utf-8">
<title>Whirl Cove – Ride Panel Graphics</title>
<link href="https://fonts.googleapis.com/css2?family=Saira+Condensed:wght@800&display=swap" rel="stylesheet">
<style>
  :root{
    --ink:#000000;
    --paper:#ffffff;
    --cove-blue:#00aeef;
    --volt-green:#72c21a;
    --trim:#8cd43a;
  }
  *{box-sizing:border-box;margin:0;padding:0}
  html,body{width:1200px;height:1200px;overflow:hidden;background:var(--paper)}
  .sheet{position:relative;width:1200px;height:1200px;font-family:"Saira Condensed",sans-serif;font-weight:800}

  .side-panel{position:absolute;top:161px;width:292px;height:231px;border:1px solid var(--trim);background:var(--paper);overflow:hidden}
  .side-panel--left{left:159px}
  .side-panel--right{left:743px}
  .side-panel__corners{position:absolute;inset:0;width:100%;height:100%}
  .brand-stack{position:absolute;left:0;right:0;top:34px;display:flex;flex-direction:column;align-items:center;color:var(--ink);line-height:.86;text-transform:uppercase}
  .brand-stack__name{font-size:68px;letter-spacing:1px}
  .brand-stack__tagline{font-size:19px;margin-top:8px;letter-spacing:.5px}

  .front-panel{position:absolute;top:514px;width:475px;height:346px}
  .front-panel--left{left:57px}
  .front-panel--right{left:662px}
  .front-panel svg{display:block;width:100%;height:100%}
  .front-panel .brand-stack{top:36px;left:auto;right:56px;width:100px}
  .front-panel .brand-stack__name{font-size:31px;letter-spacing:.5px}
  .front-panel .brand-stack__tagline{font-size:9px;margin-top:4px}

  .trailer-strip{position:absolute;height:40px;background:var(--ink);display:flex;align-items:center;color:var(--paper);font-size:38px;text-transform:uppercase;letter-spacing:1px;white-space:nowrap}
  .trailer-strip--short{left:237px;top:945px;width:818px}
  .trailer-strip--long{left:21px;top:1041px;width:1164px}
  .trailer-strip__name{position:absolute;transform:translateX(-50%);line-height:1}
</style>
</head>
<body>
<main class="sheet">

  <section class="side-panel side-panel--left" aria-label="Side panel">
    <svg class="side-panel__corners" viewBox="0 0 467 369" preserveAspectRatio="none" role="img" aria-label="Circuit-style corner graphics in black, blue and green">
      <defs>
        <linearGradient id="cornerTone" x1="0" y1="0" x2="1" y2="1">
          <stop offset="0" stop-color="#000"/>
          <stop offset=".55" stop-color="#00aeef"/>
          <stop offset="1" stop-color="#72c21a"/>
        </linearGradient>
      </defs>
      <polygon points="359,0 434,0 467,48 467,172" fill="url(#cornerTone)"/>
      <polygon points="0,208 100,369 0,369" fill="url(#cornerTone)"/>
      <polygon points="467,286 467,369 380,369" fill="url(#cornerTone)"/>
    </svg>
    <div class="brand-stack">
      <span class="brand-stack__name">Whirl</span>
      <span class="brand-stack__name">Cove</span>
      <span class="brand-stack__tagline">Revel in Bloom</span>
    </div>
  </section>

  <section class="side-panel side-panel--right" aria-label="Side panel">
    <svg class="side-panel__corners" viewBox="0 0 467 369" preserveAspectRatio="none" role="img" aria-label="Circuit-style corner graphics in black, blue and green">
      <polygon points="359,0 434,0 467,48 467,172" fill="url(#cornerTone)"/>
      <polygon points="0,208 100,369 0,369" fill="url(#cornerTone)"/>
      <polygon points="467,286 467,369 380,369" fill="url(#cornerTone)"/>
    </svg>
    <div class="brand-stack">
      <span class="brand-stack__name">Whirl</span>
      <span class="brand-stack__name">Cove</span>
      <span class="brand-stack__tagline">Revel in Bloom</span>
    </div>
  </section>

  <section class="front-panel front-panel--left" aria-label="Front panel">
    <svg viewBox="0 0 760 554" role="img" aria-label="Circuit-style graphics in green, black and blue across the front panel">
      <defs>
        <linearGradient id="circuitTone" x1="0" y1="0" x2="0" y2="1">
          <stop offset="0" stop-color="#fff"/>
          <stop offset=".22" stop-color="#eef8e2"/>
          <stop offset=".38" stop-color="#72c21a"/>
          <stop offset=".52" stop-color="#050505"/>
          <stop offset=".72" stop-color="#00aeef"/>
          <stop offset=".9" stop-color="#050505"/>
        </linearGradient>
      </defs>
      <path d="M0,0 H208 C250,0 270,40 279,73 V151 H473 V73 C478,25 510,0 553,0 H760 V370 L511,554 H237 L0,370 Z" fill="url(#circuitTone)" stroke="var(--trim)" stroke-width="1.5"/>
    </svg>
  </section>

  <section class="front-panel front-panel--right" aria-label="Front panel">
    <svg viewBox="0 0 760 554" role="img" aria-label="Circuit-style graphics in green, black and blue across the front panel">
      <path d="M0,0 H208 C250,0 270,40 279,73 V151 H473 V73 C478,25 510,0 553,0 H760 V370 L511,554 H237 L0,370 Z" fill="url(#circuitTone)" stroke="var(--trim)" stroke-width="1.5"/>
    </svg>
    <div class="brand-stack">
      <span class="brand-stack__name">Whirl</span>
      <span class="brand-stack__name">Cove</span>
      <span class="brand-stack__tagline">Revel in Bloom</span>
    </div>
  </section>

  <section class="trailer-strip trailer-strip--short" aria-label="Trailer strip 120 inch">
    <span class="trailer-strip__name" style="left:50%">Whirl Cove</span>
  </section>

  <section class="trailer-strip trailer-strip--long" aria-label="Trailer strip 171.5 inch">
    <span class="trailer-strip__name" style="left:24%">Whirl Cove</span>
    <span class="trailer-strip__name" style="left:79.5%">Whirl Cove</span>
  </section>

</main>
</body>
</html>
```